Flat Belly Design Graphics for Social

I want to create 9 social media graphics (new Instagram size 4:5 (1080 x 1350 pixels) focusing on our Flat Belly Graphics, using the pics attached. Use the attached pics, NO RANDOM STOCK PHOTOGRAPHY. For the color scheme of the graphics, the color palette is attached. YOU MUST POST ALL 9 GRAPHICS IN ONE ENTRY.
Using the 3 titles below, create one set of graphics. 1) with all text, then for the others, use the pictures as detailed below in IMPORTANT:
1. 21-Night Lean Middle Reboot Beyond 50
2. The 20-Second Trim-Core Menu Guide
3. Starlet Tricks to a Slender Midline Beyond 50 - Zero Scalpel Needed
IMPORTANT:
Only use RK Pic 1 and RK Pic 2 with the title, 21-Night Lean Middle Reboot Beyond 50
Only use meal plan1 and meal plan2 pics with the title, 20-Second Trim-Core Menu Guide
Only use starlet tricks 1 and starlet tricks 2 pics with the title, Starlet Tricks to a Slender Midline Beyond 50 - Zero Scalpel Needed
women over 40

```html
<!DOCTYPE html>
<html lang="en">
<head>
<meta charset="UTF-8">
<title>21-Night Lean Middle Reboot Beyond 50</title>
<link rel="stylesheet" href="https://fonts.googleapis.com/css2?family=Kaushan+Script&family=Raleway:wght@800;900&display=block">
<style>
  :root {
    --bg-blush: #f8dde5;
    --bg-glow: #fdf0f3;
    --ink-forest: #2e4a47;
    --accent-pink: #f07aa6;
    --accent-rose: #d5508c;
    --photo-hair: #3a2a26;
    --photo-skin: #a9765a;
    --photo-knit: #efe7e3;
    --photo-denim: #24222a;
  }
  html, body {
    margin: 0;
    padding: 0;
    width: 959px;
    height: 1200px;
    overflow: hidden;
    background: var(--bg-blush);
  }
  .post {
    position: relative;
    width: 959px;
    height: 1200px;
    overflow: hidden;
    background: radial-gradient(ellipse 62% 52% at 50% 55%, var(--bg-glow) 0%, var(--bg-blush) 100%);
    font-family: "Raleway", "Arial Black", sans-serif;
  }
  .headline {
    position: absolute;
    left: 0;
    right: 0;
    margin: 0;
    text-align: center;
    color: var(--ink-forest);
    font-weight: 900;
    line-height: 1;
    white-space: nowrap;
    letter-spacing: -1px;
  }
  .headline--days {
    top: 64px;
    font-size: 134px;
  }
  .headline--focus {
    top: 212px;
    font-size: 120px;
  }
  .script-tag {
    position: absolute;
    left: 0;
    right: 0;
    top: 312px;
    margin: 0;
    text-align: center;
    font-family: "Kaushan Script", "Brush Script MT", cursive;
    font-size: 96px;
    line-height: 1.1;
    color: var(--accent-pink);
    white-space: nowrap;
    transform: rotate(-3deg);
  }
  .script-tag__underline {
    position: absolute;
    left: 390px;
    top: 428px;
  }
  .subhead {
    position: absolute;
    left: 0;
    right: 0;
    top: 458px;
    margin: 0;
    text-align: center;
    color: var(--accent-rose);
    font-weight: 800;
    font-size: 43px;
    line-height: 58px;
    letter-spacing: -0.5px;
    white-space: nowrap;
  }
  .coach-photo {
    position: absolute;
    left: 258px;
    top: 568px;
    width: 478px;
    height: 632px;
    border-radius: 50% 50% 6% 6% / 28% 28% 0 0;
    background: linear-gradient(180deg,
      var(--photo-hair) 0%,
      var(--photo-skin) 25%,
      var(--photo-knit) 45%,
      var(--photo-knit) 65%,
      var(--photo-skin) 78%,
      var(--photo-denim) 92%);
  }
</style>
</head>
<body>
  <main class="post">
    <h1 class="headline headline--days">21-NIGHT</h1>
    <h1 class="headline headline--focus">LEAN MIDDLE</h1>
    <p class="script-tag">Reboot Beyond 50</p>
    <svg class="script-tag__underline" width="180" height="16" viewBox="0 0 180 16" aria-hidden="true">
      <path d="M2 13 C 50 4, 125 2, 178 7" fill="none" stroke="var(--accent-pink)" stroke-width="4" stroke-linecap="round"/>
    </svg>
    <p class="subhead">THE HIDDEN REASONS<br>YOU CAN’T LOSE THE BELLY FAT</p>
    <div class="coach-photo" role="img" aria-label="Photo of the smiling coach in a white cropped sweater and dark high-waisted jeans, pointing down at her toned midsection"></div>
  </main>
</body>
</html>
```